Delicious BBQ Sauce package design!

We need a corner-pouch doypack (see attached) design that aligns with our logo (which is a cartoon and intended to depict a fun and delicious bbq sauce) and can accommodate three variants of the sauce (maybe just changing the name of the sauce and adding a slight visual differentiator?). The design needs to include the following:
1. "Spicin' it up since '96!" as banner
2. Logo
3. Name of sauce (as the differentiator. There are three): Harbor Blend, Cinder Blend, Summit Blend
4. "Zesty and Tangy BBQ Sauce"
5. Actual image of bbq sauce (close up, not in container) as background to entire package. Samples attached. Let me know if you have a better idea!
6. UPC code (different for each sauce variant)
7. Company URL: www.dorvanmeats.com
8. Splash for "First Place Sauce Winner at MTDL event!" with small image of the trophy. Attached.
9. Nutrition panel and ingredients
10. QR Code

Also open to your suggestions to make this packaging great!

Target Market(s)

People who love bbq sauce

Industry/Entity Type

Retail

Font styles to use
Sans Serif

Colors

Designer to choose colors to be used in the design.

Requirements
Must have
• The design needs to include the following:
• 1. "Spicin' it up since '96!" as banner
• 2. Logo
• 3. Name of sauce (as the differentiator. There are three): Harbor Blend, Cinder Blend, Summit Blend
• 4. "Zesty and Tangy BBQ Sauce"
• 5. Actual image of bbq sauce (close up, not in container) as background to entire package. Samples attached. Let me know if you have a better idea!
• 6. UPC code (different for each sauce variant)
• 7. Company URL: www.dorvanmeats.com
• 8. Splash for "First Place Sauce Winner at MTDL event!" with small image of the trophy. Attached.
• 9. Nutrition panel and ingredients
• 10. QR Code
Nice to have
• Open to suggestions that will make packaging appealing and will get people to buy it.

```html
<!DOCTYPE html>
<html lang="en">
<head>
<meta charset="utf-8">
<title>Dorvan Grill BBQ Sauce – Harbor Blend Pouch</title>
<link rel="stylesheet" href="https://fonts.googleapis.com/css2?family=Bebas+Neue&family=Oswald:wght@500&family=Yellowtail&display=swap">
<style>
  :root {
    --stage: #d9d9d9;
    --maroon-deep: #3a0508;
    --maroon: #6e0a10;
    --red: #b0141c;
    --red-bright: #d8261e;
    --gold: #e8a920;
    --gold-light: #f6c33a;
    --white: #f4f1ee;
    --flame-yellow: #ffd21f;
    --flame-orange: #f07a12;
    --sauce-dark: #8e1206;
    --sauce: #d4330f;
    --sauce-light: #ec5a1c;
  }
  html, body {
    margin: 0;
    width: 1200px;
    height: 1200px;
    overflow: hidden;
    background: var(--stage);
  }
  .canvas {
    position: relative;
    width: 1200px;
    height: 1200px;
  }
  .pouch {
    position: absolute;
    left: 300px;
    top: 165px;
    width: 600px;
    height: 895px;
    clip-path: polygon(0 190px, 180px 0, 100% 0, 100% 100%, 0 100%);
    background:
      radial-gradient(ellipse 70% 55% at 50% 72%, var(--red-bright) 0%, var(--red) 35%, var(--maroon) 70%, var(--maroon-deep) 100%);
    overflow: hidden;
  }
  .banner {
    position: absolute;
    left: 0;
    top: 0;
    width: 600px;
    height: 200px;
  }
  .banner-text {
    font-family: "Oswald", sans-serif;
    font-weight: 500;
    font-size: 30px;
    fill: var(--white);
  }
  .brand {
    position: absolute;
    left: 0;
    top: 93px;
    width: 600px;
    text-align: center;
  }
  .brand-mark {
    display: block;
    width: 122px;
    height: 122px;
    margin: 0 auto;
    border-radius: 50%;
    background: var(--gold);
  }
  .brand-name {
    display: block;
    margin-top: 2px;
    font-family: "Bebas Neue", sans-serif;
    font-size: 36px;
    line-height: 1;
    color: var(--gold-light);
  }
  .title-frame {
    position: absolute;
    left: 70px;
    top: 273px;
    width: 446px;
    height: 146px;
    border: 2px solid var(--white);
    border-top: none;
    border-radius: 0 0 8px 8px;
    box-sizing: border-box;
  }
  .title-frame::before,
  .title-frame::after {
    content: "";
    position: absolute;
    top: 0;
    height: 2px;
    background: var(--white);
  }
  .title-frame::before { left: -2px; width: 66px; }
  .title-frame::after { right: -2px; width: 64px; }
  .tagline {
    position: absolute;
    left: 0;
    top: 244px;
    width: 600px;
    text-align: center;
    font-family: "Yellowtail", cursive;
    font-size: 50px;
    line-height: 1;
    color: var(--white);
  }
  .tagline .and {
    font-size: 18px;
    color: var(--gold);
    padding: 0 3px;
  }
  .product-name {
    position: absolute;
    left: 70px;
    top: 305px;
    width: 446px;
    text-align: center;
    font-family: "Bebas Neue", sans-serif;
    font-size: 106px;
    line-height: 1;
    color: var(--gold);
    letter-spacing: 3px;
  }
  .variant {
    position: absolute;
    left: 0;
    top: 424px;
    width: 600px;
    text-align: center;
    font-family: "Bebas Neue", sans-serif;
    font-size: 46px;
    line-height: 1;
    color: var(--white);
    letter-spacing: 6px;
  }
  .flames {
    position: absolute;
    left: 0;
    top: 479px;
    width: 600px;
    height: 156px;
    background: linear-gradient(to bottom, rgba(255,210,31,0) 0%, var(--flame-yellow) 35%, var(--flame-orange) 75%, var(--red-bright) 100%);
  }
  .sauce {
    position: absolute;
    left: 0;
    top: 635px;
    width: 600px;
    height: 260px;
    background: radial-gradient(ellipse 80% 70% at 50% 40%, var(--sauce-light) 0%, var(--sauce) 50%, var(--sauce-dark) 100%);
  }
</style>
</head>
<body>
<main class="canvas">
  <section class="pouch">
    <svg class="banner" viewBox="0 0 600 200" aria-hidden="true">
      <path d="M260 52 C 400 66, 530 110, 600 150 L 600 168 C 520 124, 400 80, 260 52 Z" fill="var(--gold)"/>
      <text class="banner-text" x="356" y="70" textLength="226" lengthAdjust="spacingAndGlyphs" transform="rotate(12 356 70)">SPICIN’ IT UP SINCE ’96!</text>
    </svg>

    <div class="brand">
      <span class="brand-mark"></span>
      <span class="brand-name">Dorvan Grill</span>
    </div>

    <div class="title-frame"></div>
    <div class="tagline">Zesty<span class="and">And</span>Tangy</div>
    <div class="product-name">BBQ SAUCE</div>
    <div class="variant">HARBOR BLEND</div>

    <div class="flames" role="img" aria-label="Illustrated grill flames over a barbecue grate"></div>
    <div class="sauce" role="img" aria-label="Close-up photograph of thick red barbecue sauce"></div>
  </section>
</main>
</body>
</html>
```